High-end Oceanfront Real Estate Group Needs Clean, Modern Web Design

I’m looking for a clean, professional, modern and beautiful homepage web design for a Real Estate group in Southern California, USA.

The group/company is “Marlow on the Shore,” and they specialize in high end (i.e. expensive), oceanfront real estate in the Orange County area.

The look and feel of the page should accentuate the brand qualities: luxurious/expensive, professional, and beautiful (Orange County is one of the most beautiful areas in all the US and we would love the site to emphasize the beautiful beaches and scenery it has to offer).

Looks we like:
• www.brantleyhomesrealty.example
• www.keptbyfenwick.example -- I think the design is pretty out-dated in this site, but I like the organization/layout of the site

Header Tags (I don’t know if we can fit all of these, may need a side-menu, but I’d prefer header title only if possible):
• Welcome
• Featured Listings
• Previously Sold
• Sell
• Property Search
• Team
• Videos
• Blog
• Explore O.C.
• Contact

I have attached the beach and logo pics that we would like to use as the header, a few pictures of the team, and one sample home/view pic which can be used in any of the other sections (for pictures of the homes, just find expensive oceanfront houses and that will be fine).

I promise to provide feedback to each and every design submission. I appreciate the hard work that all of you are putting into your designs. There can be only one contest winner, but I hope to give all of you helpful feedback to submit the best designs possible!

Target Market(s)

Very wealthy home owners of oceanfront properties. These properties are worth several millions of dollars, and thus the site and brand needs to be targeted to very wealthy, successful individuals and families (both US and international buyers).

Industry/Entity Type

Real Estate

Number of Pages Required

2 page

Requirements
Must have
• I don’t want to give too many requirements, because I want to let you all be creative. However, here are the few Must Haves:
• Must submit 2 page designs (a home page and a sub page)
• Must use logo provided
• Focus is mostly on homes, but I would like to include some beach/ocean imagery as well
• The first “item” on the home page should be an accordion/slider which shows pictures of homes and with 1 line of text: “List with the Leader” and two link buttons: “Sell Your Home” and “Buy Your Home”
• Color palette needs to be mainly blues--to match ocean and sky blue
• Exported in all major formats (psd,ai,eps,png,jpeg,etc)
Nice to have
• We don’t necessarily need all of these, but would like to feature most:
• List of videos
• “Meet the Team”—brief team bios and pics
• Link(s) to Blog
• “List with the Leader” – section on why they should choose this firm
• Featured Listings
• Previously Sold

```html
<!DOCTYPE html>
<html lang="en">
<head>
<meta charset="utf-8">
<title>Marlow on the Shore — Oceanfront Real Estate</title>
<link href="https://fonts.googleapis.com/css2?family=Open+Sans:ital,wght@0,300;0,400;0,600;0,700;1,400&display=swap" rel="stylesheet">
<style>
:root{
  --teal:#56c3c9;
  --teal-dark:#3aa9b0;
  --sky:#22aee4;
  --navy:#17324a;
  --ink:#2a2f33;
  --grey:#7d858a;
  --line:#d9dde0;
  --white:#ffffff;
  --panel:rgba(22,36,48,.78);
  --footer:#143a47;
}
*{margin:0;padding:0;box-sizing:border-box}
html,body{width:1200px;height:4265px;overflow:hidden}
body{position:relative;font-family:"Open Sans",Arial,sans-serif;color:var(--ink);background:var(--white)}
.abs{position:absolute}
section,header,footer{position:absolute;left:0;width:1200px}

/* nav */
.topnav{top:0;height:57px;background:var(--white);z-index:5;box-shadow:0 1px 3px rgba(0,0,0,.15)}
.topnav ul{list-style:none;position:absolute;left:131px;top:0;display:flex;height:57px}
.topnav li{font-size:15px;font-weight:600;letter-spacing:.3px;padding:0 17px;line-height:57px;color:var(--ink)}
.topnav li.active{border-bottom:3px solid var(--teal);color:var(--navy)}
.call{position:absolute;left:873px;top:0;width:193px;height:57px;background:var(--navy);color:var(--white);display:flex;align-items:center;padding-left:14px;gap:10px}
.call .label{font-size:8px;letter-spacing:1px;color:var(--teal);display:block;line-height:10px}
.call .num{font-size:20px;font-weight:400;line-height:22px}

/* hero */
.hero{top:0;height:805px;background:
  linear-gradient(180deg,rgba(20,60,80,0) 0%,rgba(10,40,60,.15) 100%),
  linear-gradient(180deg,#7ec0e0 0%,#a9d7ea 30%,#d9eef2 45%,#6cc7c8 55%,#2ba6b4 72%,#1c7f93 100%)}
.hero .palms-left{left:0;top:57px;width:330px;height:430px;background:radial-gradient(ellipse at 20% 60%,rgba(40,80,40,.55),rgba(40,80,40,0) 70%)}
.hero .palms-right{right:0;top:57px;width:470px;height:430px;background:radial-gradient(ellipse at 70% 50%,rgba(30,70,35,.6),rgba(30,70,35,0) 70%)}
.brand{left:131px;top:120px;display:flex;align-items:center;gap:16px;color:var(--white);font-size:44px;font-weight:400;line-height:56px}
.brand i{width:44px;height:44px;background:var(--white)}
.hero h1{left:131px;top:448px;font-size:56px;font-weight:400;line-height:64px;color:var(--white);letter-spacing:1px;text-transform:uppercase}
.hero .sub{left:131px;top:588px;font-size:34px;font-weight:300;color:var(--white);letter-spacing:.5px;text-transform:uppercase}
.btn{position:absolute;top:660px;height:56px;background:rgba(24,52,60,.88);color:var(--white);font-size:26px;font-weight:400;display:flex;align-items:center;padding-left:22px;gap:16px;text-transform:uppercase}
.btn.sell{left:131px;width:316px}
.btn.buy{left:489px;width:316px}
.dots{left:165px;top:772px;display:flex;gap:16px;z-index:3}
.dots span{width:54px;height:54px;border-radius:50%;background:var(--navy);color:var(--white);font-size:17px;font-weight:600;display:flex;align-items:center;justify-content:center;border:3px solid #2a5578}

/* welcome */
.welcome{top:805px;height:531px}
.welcome .title{left:0;width:1200px;top:73px;display:flex;justify-content:center;align-items:center;gap:20px}
.welcome .title .lead{font-size:50px;font-weight:300;color:var(--ink);letter-spacing:1px}
.welcome .title .boxed{background:var(--teal);color:var(--white);font-size:44px;font-weight:300;padding:0 22px;line-height:86px;text-transform:uppercase}
.welcome .rule{left:272px;top:176px;width:740px;height:1px;background:var(--line)}
.welcome .tag{left:0;width:1200px;top:190px;text-align:center;font-size:16px;font-style:italic;color:var(--grey)}
.welcome .copy{left:171px;top:260px;width:580px;font-size:13.5px;line-height:20px;color:var(--grey)}
.welcome .copy p{margin-bottom:18px}
.more{font-size:12px;font-weight:600;color:var(--teal);text-transform:uppercase;letter-spacing:.5px}
.photo-circle{position:absolute;border-radius:50%;border:4px solid var(--white);box-shadow:0 2px 6px rgba(0,0,0,.2)}
.pc1{left:762px;top:262px;width:176px;height:176px;background:linear-gradient(135deg,#3e4a55,#6f8d9e 50%,#2b5b73)}
.pc2{left:880px;top:240px;width:150px;height:150px;background:linear-gradient(160deg,#cfe3ee,#5d8fab 55%,#243948)}

/* search */
.search{top:1336px;height:546px;background:linear-gradient(180deg,#2a3a4a 0%,#4f6472 45%,#7a8a8e 70%,#3a4a52 100%)}
.search-panel{left:131px;top:63px;width:367px;height:421px;background:var(--panel)}
.search-panel h3{height:52px;background:var(--teal);color:var(--white);font-size:22px;font-weight:400;line-height:52px;padding-left:22px}
.select{position:absolute;left:28px;width:310px;height:38px;border:1px solid rgba(255,255,255,.55);color:var(--white);font-size:13px;line-height:36px;padding-left:12px}
.select i{position:absolute;right:0;top:0;width:34px;height:36px;border-left:1px solid rgba(255,255,255,.55);display:flex;align-items:center;justify-content:center}
.search-go{position:absolute;left:307px;top:372px;width:60px;height:57px;background:var(--teal);display:flex;align-items:center;justify-content:center}
.want{left:529px;top:67px;width:540px;color:var(--white)}
.want h2{font-size:44px;font-weight:300;line-height:60px}
.want p{font-size:13.5px;line-height:20px;margin-top:6px}
.tabs-bs{left:529px;top:216px;display:flex}
.tabs-bs span{width:97px;height:46px;background:var(--teal);color:var(--white);font-size:20px;line-height:46px;text-align:center}
.tabs-bs span+span{background:var(--teal-dark)}
.types{left:529px;top:262px;width:537px;height:150px;background:var(--panel);display:flex;justify-content:space-around;align-items:center;padding:0 20px}
.types div{display:flex;flex-direction:column;align-items:center;gap:10px;color:var(--white);font-size:12px;text-transform:uppercase}

/* listings */
.listings{top:1882px;height:569px;background:var(--white)}
.ltabs{left:162px;top:60px;width:870px;height:66px;border-bottom:1px solid var(--line)}
.ltabs span{position:absolute;top:8px;font-size:32px;font-weight:300;color:var(--ink);line-height:52px}
.ltabs .on{left:0;top:0;width:316px;height:66px;background:var(--sky);transform:skewX(-12deg)}
.ltabs .on b{display:block;transform:skewX(12deg);font-size:32px;font-weight:300;color:var(--white);text-align:center;line-height:66px}
.ltabs .sep{position:absolute;top:12px;width:1px;height:44px;background:var(--line)}
.card{position:absolute;top:191px;width:285px;height:315px;border:1px solid var(--teal);background:var(--white)}
.card .img{height:200px;position:relative}
.card .price{position:absolute;right:0;bottom:0;background:rgba(20,30,36,.75);color:var(--white);font-size:22px;font-weight:600;padding:4px 14px}
.card h4{font-size:21px;font-weight:400;color:var(--teal);padding:8px 0 0 12px;line-height:26px}
.card .loc{font-size:15px;color:var(--grey);padding-left:12px}
.card .foot{position:absolute;left:0;right:0;bottom:0;height:40px;border-top:1px solid var(--line);display:flex;align-items:center;font-size:12px;color:var(--ink);padding-left:12px;gap:22px}
.card .foot i{position:absolute;right:0;top:0;width:40px;height:40px;background:var(--sky);display:flex;align-items:center;justify-content:center}
.chev{position:absolute}

/* videos */
.videos{top:2451px;height:543px;background:linear-gradient(180deg,#2f4650 0%,#4b6670 35%,#8aa4a8 62%,#2c5664 85%,#1d3c47 100%)}
.videos h2{left:0;width:1200px;top:50px;text-align:center;font-size:50px;font-weight:300;color:var(--white)}
.videos p{left:200px;width:800px;top:140px;text-align:center;font-size:13px;line-height:18px;color:var(--white)}
.play{left:530px;top:239px}
.social-row{left:325px;top:438px;width:550px;height:56px;display:flex;justify-content:space-between;align-items:center}
.social-row::before{content:"";position:absolute;left:20px;right:20px;top:28px;height:1px;background:rgba(255,255,255,.5)}
.social-row span{position:relative;width:56px;height:56px;border-radius:50%;background:#2a7ab8;border:3px solid rgba(255,255,255,.35)}

/* team */
.team{top:2994px;height:475px}
.team h2{left:151px;top:52px;font-size:50px;font-weight:300;color:var(--ink)}
.member{position:absolute;top:158px;width:240px;text-align:center}
.member .face{width:190px;height:190px;border-radius:50%;margin:0 auto;border:3px solid #eef0f1}
.member h5{font-size:22px;font-weight:400;color:var(--teal);margin-top:14px;line-height:28px}
.member small{display:block;font-size:12px;color:var(--ink);padding-bottom:6px;border-bottom:1px solid var(--line);width:150px;margin:0 auto}

/* blog */
.blog{top:3469px;height:369px;border-top:1px solid var(--line)}
.blog h2{left:134px;top:30px;font-size:50px;font-weight:300;color:var(--ink)}
.post{position:absolute;top:136px;width:270px}
.post .date{position:absolute;left:0;top:0;width:68px;height:68px;background:var(--sky);color:var(--white);text-align:center;font-size:22px;font-weight:600;line-height:30px;padding-top:6px}
.post .date small{display:block;font-size:13px;font-weight:400;line-height:16px}
.post h6{margin-left:80px;font-size:17px;font-weight:400;color:var(--ink);line-height:22px}
.post .by{margin-left:80px;font-size:8px;color:var(--grey);margin-top:2px}
.post p{margin-top:22px;font-size:12px;line-height:17px;color:var(--grey)}
.post .more{display:block;margin-top:10px}

/* contact */
.contact{top:3838px;height:364px;background:linear-gradient(180deg,#1d6174 0%,#1b5566 60%,#174a59 100%)}
.contact h2{left:0;width:1200px;top:48px;text-align:center;font-size:34px;font-weight:400;color:var(--white);letter-spacing:1px}
.contact .rule{left:0;width:1200px;top:112px;height:1px;background:rgba(255,255,255,.2)}
.cinfo{position:absolute;top:140px;width:340px;text-align:center;color:var(--white)}
.cinfo .ic{width:64px;height:64px;border-radius:50%;background:var(--white);margin:0 auto;display:flex;align-items:center;justify-content:center}
.cinfo .big{font-size:34px;font-weight:300;margin-top:30px}
.cinfo .addr{font-size:22px;font-weight:300;margin-top:24px;line-height:26px}
.cinfo .addr small{display:block;font-size:14px;line-height:17px}
.cinfo .mail{font-size:24px;font-weight:300;margin-top:34px}
footer{top:4202px;height:63px;background:var(--footer);color:rgba(255,255,255,.75);font-size:13px;text-align:center;line-height:63px}
</style>
</head>
<body>

<header class="topnav">
  <ul>
    <li class="active">HOME</li><li>PROPERTIES</li><li>SEARCH</li><li>VIDEOS</li><li>OUR TEAM</li><li>BLOG</li><li>CONTACT US</li>
  </ul>
  <div class="call">
    <svg width="30" height="30" viewBox="0 0 30 30"><circle cx="15" cy="15" r="14" fill="none" stroke="#56c3c9" stroke-width="2"/><path d="M10 8c1 0 2 3 2 4s-2 1-1 3 3 4 4 4 1-2 2-2 4 1 4 2-2 3-4 3c-4 0-10-6-10-10 0-2 2-4 3-4z" fill="#56c3c9"/></svg>
    <div><span class="label">CALL US NOW</span><span class="num">555.014.2290</span></div>
  </div>
</header>

<section class="hero" role="img" aria-label="Tropical beach with palm trees, white sand and turquoise ocean water">
  <div class="abs palms-left"></div>
  <div class="abs palms-right"></div>
  <div class="abs brand"><i></i><span>Marlow on the Shore</span></div>
  <h1 class="abs">Looking for a luxurious<br>&amp; beautiful home</h1>
  <div class="abs sub">Now it's easy to find your future home</div>
  <div class="btn sell">Sell your home
    <svg width="30" height="30" viewBox="0 0 30 30"><circle cx="15" cy="15" r="13" fill="none" stroke="#fff" stroke-width="2"/><path d="M13 9l6 6-6 6" fill="none" stroke="#fff" stroke-width="2.5"/></svg></div>
  <div class="btn buy">Buy your home
    <svg width="30" height="30" viewBox="0 0 30 30"><circle cx="15" cy="15" r="13" fill="none" stroke="#fff" stroke-width="2"/><path d="M13 9l6 6-6 6" fill="none" stroke="#fff" stroke-width="2.5"/></svg></div>
</section>
<div class="abs dots"><span>1</span><span>2</span><span>3</span></div>

<section class="welcome">
  <div class="abs title"><span class="lead">WELCOME TO</span><span class="boxed">Marlow on the shore</span></div>
  <div class="abs rule"></div>
  <div class="abs tag">The best place to get all kind of luxurious homes at sea view</div>
  <div class="abs copy">
    <p>Lorem ipsum dolor sit amet, consectetuer adipiscing elit, sed diam nonummy nibh euismod tincidunt ut laoreet dolore magna aliquam erat volutpat. Ut wisi enim ad minim veniam, quis nostrud exerci tation ullamcorper suscipit lobortis nisl ut aliquip ex ea commodo consequat. Duis autem vel eum iriure dolor in hendrerit in vulputate velit esse molestie consequat, vel illum dolore eu feugiat nulla facilisis at vero eros et accumsan et iusto odio dignissim qui blandit praesent luptatum zzril delenit augue duis dolore te feugait nulla facilisi.</p>
    <p>Lorem ipsum dolor sit amet, consectetuer adipiscing elit, sed diam nonummy nibh euismod tincidunt ut laoreet dolore magna aliquam erat volutpat.</p>
    <span class="more">Read more ›</span>
  </div>
  <div class="photo-circle pc1" role="img" aria-label="Luxury home interior with pool view"></div>
  <div class="photo-circle pc2" role="img" aria-label="Modern oceanfront villa terrace"></div>
</section>

<section class="search" role="img" aria-label="Blurred view of a white luxury villa among trees">
  <div class="abs search-panel">
    <h3>Search Property</h3>
    <div class="select" style="top:110px">Location<i><svg width="12" height="8"><path d="M1 1l5 5 5-5" fill="none" stroke="#fff" stroke-width="2"/></svg></i></div>
    <div class="select" style="top:166px">Sub - location<i><svg width="12" height="8"><path d="M1 1l5 5 5-5" fill="none" stroke="#fff" stroke-width="2"/></svg></i></div>
    <div class="select" style="top:222px">District<i><svg width="12" height="8"><path d="M1 1l5 5 5-5" fill="none" stroke="#fff" stroke-width="2"/></svg></i></div>
    <div class="select" style="top:277px">Place From<i><svg width="12" height="8"><path d="M1 1l5 5 5-5" fill="none" stroke="#fff" stroke-width="2"/></svg></i></div>
    <div class="select" style="top:333px">Place To<i><svg width="12" height="8"><path d="M1 1l5 5 5-5" fill="none" stroke="#fff" stroke-width="2"/></svg></i></div>
    <div class="search-go"><svg width="26" height="26" viewBox="0 0 26 26"><circle cx="11" cy="11" r="7" fill="none" stroke="#fff" stroke-width="2.5"/><path d="M16 16l7 7" stroke="#fff" stroke-width="3"/></svg></div>
  </div>
  <div class="abs want">
    <h2>I Want To...</h2>
    <p>Lorem ipsum dolor sit amet, consectetuer adipiscing elit, sed diam nonummy nibh euismod. Lorem ipsum dolor sit amet, consectetuer adipiscing elit, sed diam nonummy nibh euismod. Lorem ipsum dolor sit amet.</p>
  </div>
  <div class="abs tabs-bs"><span>Buy</span><span>Sell</span></div>
  <div class="abs types">
    <div><svg width="54" height="54" viewBox="0 0 54 54" fill="#fff"><path d="M27 6L4 26h6v22h34V26h6z"/><rect x="22" y="34" width="10" height="14" fill="#24343f"/><rect x="14" y="30" width="6" height="6" fill="#24343f"/><rect x="34" y="30" width="6" height="6" fill="#24343f"/></svg>Villas</div>
    <div><svg width="54" height="54" viewBox="0 0 54 54" fill="#fff"><rect x="6" y="16" width="18" height="32"/><rect x="26" y="6" width="22" height="42"/><g fill="#24343f"><rect x="10" y="20" width="4" height="4"/><rect x="16" y="20" width="4" height="4"/><rect x="10" y="28" width="4" height="4"/><rect x="16" y="28" width="4" height="4"/><rect x="30" y="10" width="5" height="5"/><rect x="39" y="10" width="5" height="5"/><rect x="30" y="19" width="5" height="5"/><rect x="39" y="19" width="5" height="5"/><rect x="30" y="28" width="5" height="5"/><rect x="39" y="28" width="5" height="5"/></g></svg>Apartments</div>
    <div><svg width="54" height="54" viewBox="0 0 54 54" fill="#fff"><rect x="10" y="6" width="34" height="42"/><g fill="#24343f"><rect x="15" y="11" width="6" height="5"/><rect x="24" y="11" width="6" height="5"/><rect x="33" y="11" width="6" height="5"/><rect x="15" y="20" width="6" height="5"/><rect x="24" y="20" width="6" height="5"/><rect x="33" y="20" width="6" height="5"/><rect x="15" y="29" width="6" height="5"/><rect x="33" y="29" width="6" height="5"/><rect x="23" y="36" width="8" height="12"/></g></svg>Offices</div>
    <div><svg width="54" height="54" viewBox="0 0 54 54" fill="none" stroke="#fff" stroke-width="3"><circle cx="27" cy="25" r="18"/><path d="M9 25h36M27 7c-8 10-8 26 0 36M27 7c8 10 8 26 0 36"/><path d="M27 49l-5-6h10z" fill="#fff"/></svg>Land Plots</div>
  </div>
</section>

<section class="listings">
  <div class="abs ltabs">
    <div class="abs on"><b>Featured Listing</b></div>
    <span style="left:336px">Most Popular</span>
    <i class="sep" style="left:570px"></i>
    <span style="left:606px">Sold Out Listing</span>
  </div>
  <svg class="chev" style="left:62px;top:265px" width="36" height="110" viewBox="0 0 36 110"><path d="M34 2L4 55l30 53" fill="none" stroke="#c9cfd3" stroke-width="2"/></svg>
  <svg class="chev" style="left:1100px;top:265px" width="36" height="110" viewBox="0 0 36 110"><path d="M2 2l30 53-30 53" fill="none" stroke="#c9cfd3" stroke-width="2"/></svg>

  <div class="card" style="left:156px">
    <div class="img" role="img" aria-label="Oceanfront terrace with lounge chairs at sunset" style="background:linear-gradient(180deg,#7fb4d6 0%,#3a7fae 45%,#2d4f6a 70%,#8a5f3c 100%)"><span class="price">$ 1,495,000</span></div>
    <h4>14200 Tidewater Way</h4><div class="loc">Pacific Coast</div>
    <div class="foot"><span>⌕ View Details</span><span>▣ Photos</span><i><svg width="12" height="18"><path d="M2 2l7 7-7 7" fill="none" stroke="#fff" stroke-width="2.5"/></svg></i></div>
  </div>
  <div class="card" style="left:461px">
    <div class="img" role="img" aria-label="Luxury living room with sea view at dusk" style="background:linear-gradient(180deg,#4d6f8e 0%,#8fb1c9 40%,#d8d6d0 65%,#6c6761 100%)"><span class="price">$ 1,495,000</span></div>
    <h4>14200 Tidewater Way</h4><div class="loc">Pacific Coast</div>
    <div class="foot"><span>⌕ View Details</span><span>▣ Photos</span><i><svg width="12" height="18"><path d="M2 2l7 7-7 7" fill="none" stroke="#fff" stroke-width="2.5"/></svg></i></div>
  </div>
  <div class="card" style="left:768px">
    <div class="img" role="img" aria-label="Villa with infinity pool overlooking a bay" style="background:linear-gradient(180deg,#9cc6de 0%,#5c9ab8 40%,#3c6b4c 70%,#1e5a73 100%)"><span class="price">$ 1,495,000</span></div>
    <h4>14200 Tidewater Way</h4><div class="loc">Pacific Coast</div>
    <div class="foot"><span>⌕ View Details</span><span>▣ Photos</span><i><svg width="12" height="18"><path d="M2 2l7 7-7 7" fill="none" stroke="#fff" stroke-width="2.5"/></svg></i></div>
  </div>
</section>

<section class="videos" role="img" aria-label="Resort villa with palm trees and infinity pool facing the sea">
  <h2 class="abs">Featured Videos</h2>
  <p class="abs">Lorem ipsum dolor sit amet, consectetuer adipiscing elit, sed diam nonummy nibh euismod tincidunt ut laoreet dolore magna aliquam erat volutpat. Ut wisi enim ad minim veniam, quis nostrud exerci tation ullamcorper suscipit lobortis nisl ut aliquip ex ea commodo consequat. Duis autem vel eum iriure dolor in hendrerit in vulputate velit esse molestie consequat.</p>
  <svg class="abs play" width="140" height="140" viewBox="0 0 140 140"><circle cx="70" cy="70" r="64" fill="rgba(255,255,255,.12)" stroke="#fff" stroke-width="7"/><path d="M55 40l42 30-42 30z" fill="#fff"/></svg>
  <div class="abs social-row"><span></span><span></span><span></span><span></span><span></span><span></span></div>
</section>

<section class="team">
  <h2 class="abs">Our Team</h2>
  <svg class="chev" style="left:62px;top:225px" width="36" height="110" viewBox="0 0 36 110"><path d="M34 2L4 55l30 53" fill="none" stroke="#c9cfd3" stroke-width="2"/></svg>
  <svg class="chev" style="left:1100px;top:225px" width="36" height="110" viewBox="0 0 36 110"><path d="M2 2l30 53-30 53" fill="none" stroke="#c9cfd3" stroke-width="2"/></svg>
  <div class="member" style="left:107px"><div class="face" role="img" aria-label="Portrait of Graham Ellis" style="background:radial-gradient(circle at 50% 40%,#c9a58a,#6b4a38 75%)"></div><h5>Graham Ellis</h5><small>Marketing Manager</small></div>
  <div class="member" style="left:366px"><div class="face" role="img" aria-label="Portrait of Noreen Marlow" style="background:radial-gradient(circle at 50% 40%,#e6c9a8,#6f8db0 75%)"></div><h5>Noreen Marlow</h5><small>CEO, Director</small></div>
  <div class="member" style="left:608px"><div class="face" role="img" aria-label="Portrait of Tessa Hartwell" style="background:radial-gradient(circle at 50% 40%,#d8b48e,#8fb83a 75%)"></div><h5>Tessa Hartwell</h5><small>Sales Partner</small></div>
  <div class="member" style="left:849px"><div class="face" role="img" aria-label="Portrait of Lena Vossberg" style="background:radial-gradient(circle at 50% 40%,#e8c9a0,#5a9c3e 75%)"></div><h5>Lena Vossberg</h5><small>CEO, Director</small></div>
</section>

<section class="blog">
  <h2 class="abs">From The Blog</h2>
  <div class="post" style="left:134px"><div class="date">20<small>FEB</small></div><h6>Harbor Group Open Houses, February 21</h6><div class="by">posted by site admin</div>
    <p>Lorem ipsum dolor sit amet, consectetuer adipiscing elit, sed diam nonummy nibh euismod tincidunt ut laoreet dolore magna aliquam erat volutpat.</p><span class="more">Read more ›</span></div>
  <div class="post" style="left:455px"><div class="date">20<small>FEB</small></div><h6>Harbor Group Open Houses, February 21</h6><div class="by">posted by site admin</div>
    <p>Lorem ipsum dolor sit amet, consectetuer adipiscing elit, sed diam nonummy nibh euismod tincidunt ut laoreet dolore magna aliquam erat volutpat.</p><span class="more">Read more ›</span></div>
  <div class="post" style="left:782px"><div class="date">20<small>FEB</small></div><h6>Harbor Group Open Houses, February 21</h6><div class="by">posted by site admin</div>
    <p>Lorem ipsum dolor sit amet, consectetuer adipiscing elit, sed diam nonummy nibh euismod tincidunt ut laoreet dolore magna aliquam erat volutpat.</p><span class="more">Read more ›</span></div>
</section>

<section class="contact">
  <h2 class="abs">GET IN TOUCH</h2>
  <div class="abs rule"></div>
  <div class="cinfo" style="left:72px"><div class="ic"><svg width="26" height="26" viewBox="0 0 26 26"><path d="M6 3c1.5 0 3 4 3 5s-2 1.5-1 3.5 4 5 5.5 5 1.5-2 3-2 5 1.5 5 3-2.5 4-5 4C11 21.5 4.5 15 4.5 9 4.5 6 5 3 6 3z" fill="#3aa9b0"/></svg></div><div class="big">555.014.2290</div></div>
  <div class="cinfo" style="left:430px"><div class="ic"><svg width="26" height="30" viewBox="0 0 26 30"><path d="M13 1C6.5 1 2 5.5 2 11.5 2 19 13 29 13 29s11-10 11-17.5C24 5.5 19.5 1 13 1z" fill="#3aa9b0"/><circle cx="13" cy="11.5" r="4" fill="#fff"/></svg></div><div class="addr">Marlow Properties,<small>Lorem ipsum dolor sit amet<br>consectetuer adipiscing</small></div></div>
  <div class="cinfo" style="left:791px"><div class="ic"><svg width="28" height="20" viewBox="0 0 28 20"><rect x="1" y="1" width="26" height="18" rx="2" fill="#3aa9b0"/><path d="M2 2l12 9 12-9" fill="none" stroke="#fff" stroke-width="2"/></svg></div><div class="mail">info@marlowshore.example</div></div>
</section>

<footer>Copyright 2015 Marlow Properties. All Rights Reserved.</footer>

</body>
</html>
```